Lantern Pantry cafe promotion flyer

Lantern Pantry is a waterfront cafe/ function center with gorgeous views. Lantern Pantry is a very modern venue that can cater for 200 people (seating) and it is located in a business area.

The main customers are the professional bank employees (80%) with the remaining being other corporate workers. Lantern Pantrys main trading periods are Morning Coffee, Breakfast and Lunch with the average spend being between $5-$15 per head. Hospitality is a highly competitive market and since there is not much general foot traffic on the waterfront side during winter, Lantern Pantry have decided to advertise by sending out some flyers to all the nearby buildings, to let the Quayside Neighbourhood know where we are, what we offer and to generate new business.

We would like to design a unique flyer with a great title, plus the deals we offer, plus some pictures , would prefer fresh and bright colour which can attract people from outside the venue .You can visit our website and have a look at our venue to get some idea as well:
www.thelanternpantry.com.au

Thanks for the designs submitted so far.
but I prefer the background color is bight color, like fresh food color will be better, prefer orange, green, yellow that kind of fresh color, can entice people to come in and have their lunch or breakfast.

I would prefer to have a picture of coffee with coffee art, food change to a big sandwich or burger. The entire flyer is try to entice the customer to come in eat and drink. The flyer is going to be put on a black board, so there should be some contrast in the colour.

look forward to your new design.

Here is a sample title:
only our special offers warm up your savings

(or something similar, more creative and appealing to the potential customers)

Monday-Friday, early bird coffee 7:30a-8:30am, small for $2.80, large for $3.30.

Deals detail:
coffee with freshly home-made muffin $5.50
Coffee with egg bacon muffin $6.90
Coffee with gourmet egg bacon wrap $8.50
Coffee with fruit toast $6.50

Lunch Special:
Only $4 for a glass of wine/a bottle of beer with our daily Lunch specail
Buy any Focaccia for only $8.90 get one soft drink free

Friday Happy hour drinks 12pm-7pm,
selection of wine/beer/spirits for only $6

corporate catering and function room hire available
Waterfront Side, QVR building, 412 Wexley Street, Docklands 3008
E:catering@thelanternpantry.com.au
P:03 9481 2257

we require hi resolution PDF files of both A5 and A3 Poster

                                       

Hi all designers

but I prefer the background color  is bight color, like fresh food color will be better, prefer orange, green, yellow that kind of fresh color, can entice people to come in and have their lunch or breakfast.

I would prefer to change the coffee to a coffee with coffee art, food change to a better sandwich or burger or focaccia. The entire flyer is try to entice the customer to come in eat and drink.

will you be able to add this to it:

Also, can you please take away the live band 4p-7pm for Fridays , thanks.

Target Market(s)

the target customers are the corporates who has something quick to eat for breakfast and lunch, normally on a budget.

Industry/Entity Type

Catering

Requirements
Must have
• great food and drink pictures
Should not have
• dark colour

```html
<!DOCTYPE html>
<html lang="en">
<head>
<meta charset="utf-8">
<title>Lantern Pantry – Winter Special Offers</title>
<link href="https://fonts.googleapis.com/css2?family=Arvo:wght@700&family=Cutive&display=swap" rel="stylesheet">
<style>
  :root {
    --sunrise: #ffc94a;
    --orange: #f7901e;
    --orange-deep: #ee7a12;
    --sky-top: #8fc7e8;
    --sky-low: #ffd79a;
    --water: #f3a24a;
    --paper: #ffffff;
    --paper-shade: #ececec;
    --frame-line: #c4c4c4;
    --ink: #2e1504;
    --text-light: #ffffff;
    --lime: #b3bf2f;
    --warm-orange: #e86a2a;
    --warm-red: #b23a22;
    --dusk-blue: #5a88b8;
    --candle: #ffd27a;
  }
  * { margin: 0; padding: 0; box-sizing: border-box; }
  html, body { width: 845px; height: 1200px; overflow: hidden; background: var(--orange); }
  .flyer {
    position: relative;
    width: 845px;
    height: 1200px;
    background: linear-gradient(180deg, var(--sunrise) 0%, var(--orange) 55%, var(--orange-deep) 100%);
    color: var(--ink);
    font-family: "Cutive", "Courier New", serif;
    overflow: hidden;
  }
  .harbour-view {
    position: absolute; left: 0; top: 0; width: 845px; height: 210px;
    background: linear-gradient(180deg, var(--sky-top) 0%, var(--sky-low) 62%, var(--water) 100%);
  }
  .brand {
    position: absolute; left: 0; top: 128px; width: 845px;
    display: flex; justify-content: center; align-items: center; gap: 10px;
    font-family: "Arvo", Georgia, serif; font-weight: 700;
    font-size: 22px; letter-spacing: 2px; color: var(--ink);
    text-transform: uppercase;
  }
  .brand-dot { width: 14px; height: 14px; border-radius: 50%; background: var(--ink); }
  .tagline-banner {
    position: absolute; left: 22px; top: 188px; width: 798px; height: 84px;
    background: linear-gradient(180deg, var(--paper) 0%, var(--paper) 70%, var(--paper-shade) 100%);
    border-radius: 7px;
  }
  .tagline-banner .frame {
    position: absolute; left: 12px; top: 13px; right: 12px; bottom: 17px;
    border: 1.5px solid var(--frame-line); border-radius: 3px;
  }
  .tagline-banner p {
    position: absolute; left: 0; right: 0; top: 30px; text-align: center;
    font-family: "Arvo", Georgia, serif; font-weight: 700;
    font-size: 17px; color: var(--ink);
  }
  .venue-photo { position: absolute; left: 22px; width: 138px; }
  .venue-photo.interior {
    top: 285px; height: 312px;
    background: linear-gradient(160deg, var(--warm-orange) 0%, var(--warm-red) 50%, #f0d9b8 100%);
  }
  .venue-photo.table-setting {
    top: 597px; height: 311px;
    background: linear-gradient(180deg, var(--dusk-blue) 0%, #c9a27a 45%, var(--candle) 75%, #d98a3a 100%);
  }
  .offers { position: absolute; left: 180px; top: 0; width: 650px; }
  .offer-heading {
    position: absolute; left: 0; white-space: nowrap;
    font-family: "Arvo", Georgia, serif; font-weight: 700;
    font-size: 33px; line-height: 40px; color: var(--ink);
  }
  .offer-lines {
    position: absolute; left: 0; list-style: none; white-space: nowrap;
    font-size: 24px; line-height: 36.5px;
  }
  .daily-deals .offer-heading { top: 296px; }
  .daily-deals .offer-lines { top: 337px; }
  .lunch-special .offer-heading { top: 502px; }
  .lunch-special .offer-lines { top: 543px; }
  .happy-hour .offer-heading { top: 765px; }
  .happy-hour .offer-lines { top: 812px; }
  .early-bird, .group-booking {
    position: absolute; left: 0; width: 845px; text-align: center;
    font-size: 18px; white-space: nowrap;
  }
  .early-bird { top: 918px; }
  .group-booking { top: 954px; }
  .contact-band {
    position: absolute; left: 0; top: 1017px; width: 845px; height: 183px;
    background: var(--lime); color: var(--text-light);
  }
  .contact-block { position: absolute; top: 18px; }
  .contact-block.find { left: 35px; }
  .contact-block.reach { left: 403px; }
  .contact-block h2 {
    font-family: "Arvo", Georgia, serif; font-weight: 700;
    font-size: 33px; line-height: 40px; margin-bottom: 10px;
  }
  .contact-block p { font-size: 19px; line-height: 28.5px; white-space: nowrap; }
</style>
</head>
<body>
<main class="flyer">
  <div class="harbour-view" role="img" aria-label="Bright morning view of the waterfront harbour with city buildings"></div>
  <div class="brand"><span class="brand-dot"></span><span>Lantern Pantry</span></div>

  <header class="tagline-banner">
    <div class="frame"></div>
    <p>This winter is not so cold with Lantern Pantry's Special Offers</p>
  </header>

  <div class="venue-photo interior" role="img" aria-label="Warmly lit cafe interior with red lounge seating and round tables"></div>
  <div class="venue-photo table-setting" role="img" aria-label="Wine glasses and candles on a dining table by the harbour"></div>

  <section class="offers daily-deals">
    <h2 class="offer-heading">Daily Deals</h2>
    <ul class="offer-lines">
      <li>Coffee with freshly home-made muffin $5.50</li>
      <li>Coffee with egg bacon muffin $6.90</li>
      <li>Coffee with gourmet egg bacon wrap $8.50</li>
      <li>Coffee with fruit toast $6.50</li>
    </ul>
  </section>

  <section class="offers lunch-special">
    <h2 class="offer-heading">Lunch Special</h2>
    <ul class="offer-lines">
      <li>Only $4 for a glass of wine/a bottle</li>
      <li>of beer with our daily Lunch special.</li>
      <li>&nbsp;</li>
      <li>Buy any Focaccia for only $8.90</li>
      <li>get one soft drink free.</li>
    </ul>
  </section>

  <section class="offers happy-hour">
    <h2 class="offer-heading">Friday Afternoon Happy Hour</h2>
    <ul class="offer-lines">
      <li>Drinks 12pm-7pm</li>
      <li>selection of wine/beer/spirits for only $6</li>
    </ul>
  </section>

  <p class="early-bird">Mon-Fri early bird coffee 7:30am-8:30am: small $2.80, large $3.30</p>
  <p class="group-booking">Any group booking 8+ for breakfast /Lunch will get 10% discount</p>

  <footer class="contact-band">
    <div class="contact-block find">
      <h2>Find us</h2>
      <p>The Lantern Pantry</p>
      <p>Shop 1, 412 Wexley Street</p>
      <p>Wexley Harbour, Docklands</p>
    </div>
    <div class="contact-block reach">
      <h2>Contact us</h2>
      <p>Tel : +613 9481 2257</p>
      <p>Fax : +613 9481 2250</p>
      <p>catering@thelanternpantry.com.au</p>
    </div>
  </footer>
</main>
</body>
</html>
```